Popup Nightclub Grand Opening Flyer

We need to design a flyer for the grand opening of an upscale, exclusive nightclub called "Lanternfall". The design needs to be chic and exclusive. The background should be black and the text should primarily be white. We like minimalist designs.

Here is the text for the flyer
-
Velvetroom Atlanta Presents

Lanternfall (LOGO)

A Popup Nightclub Experience
For one night Only

Friday, October 18, 2013
Party begins at 9PM

INVITE ONLY

See invitation for location details
(Velvetroom Atlanta logo)

-
Examples we like

http://cdn2-b.plorvex-news.test/sites/default/files/styles/image_content_width/hash/3d/fb/4729105836_5521_flyer.jpg?itok=Q8rmZt2w

http://api.trevlomesh.test/files/9Kxq-Tr72PQd0hzXbwaLr8VMN2K617J3nqBw5CHR4XtdM8Y2sqEA-KjuxBnRoLW4QTyMHD8nwfYcJz-Rkh3vqp4MNaTYe9s1/7zenFridays.jpg

http://brenquist.test/wp-content/uploads/yootheme/widgetkit/gallery/7zen/7zen-gen_nvibe4-01.jpg
Updates

Hi All, one thing that we are seeing that we don't like is on over emphasis on the phrase "a popup nightclub experience" please don't make this the largest thing on the flyer

Target Market(s)

Target market is 25-35 year olds who are affluent (rich) and like luxury brands

Requirements
Must have
• Dark Background
Nice to have
• Velvetroom Logo on the bottom
Modern text that isn't curvy
Should not have
• Curved text

```html
<!DOCTYPE html>
<html lang="en">
<head>
<meta charset="utf-8">
<title>Lanternfall Nightclub — Velvetroom Atlanta</title>
<link rel="stylesheet" href="https://fonts.googleapis.com/css2?family=Comfortaa:wght@300;700&family=Poiret+One&family=Arimo:wght@700&display=swap">
<style>
  :root {
    --bg: #000000;
    --ink: #ffffff;
    --mark: #d9d9dc;
    --badge: #2b2b2b;
    --muted: #e6e6e6;
  }
  * { margin: 0; padding: 0; box-sizing: border-box; }
  html, body {
    width: 1200px; height: 1200px;
    overflow: hidden;
    background: var(--bg);
  }
  .flyer {
    position: relative;
    width: 1200px; height: 1200px;
    background: var(--bg);
    color: var(--ink);
    font-family: "Comfortaa", sans-serif;
  }
  .flyer > * { position: absolute; white-space: nowrap; }

  .presenter {
    top: 64px; left: 0; width: 1300px;
    text-align: center;
    font-weight: 700; font-size: 27px;
    letter-spacing: 0.16em;
    word-spacing: 0.25em;
  }

  .club-mark {
    top: 142px; left: 549px;
    width: 190px; height: 190px;
  }

  .club-name {
    top: 396px; left: 0; width: 1288px;
    text-align: center;
    font-weight: 300;
    color: var(--mark);
    text-transform: uppercase;
    line-height: 1.1;
  }
  .club-name .name-main { display: block; font-size: 58px; letter-spacing: 0.1em; }
  .club-name .name-sub { display: block; font-size: 33px; letter-spacing: 0.12em; margin-top: 10px; }

  .tagline {
    top: 618px; left: 196px;
    font-weight: 700; font-size: 26px;
    letter-spacing: 0.2em;
    word-spacing: 0.3em;
  }

  .deco {
    font-family: "Poiret One", sans-serif;
    text-transform: uppercase;
    color: transparent;
    -webkit-text-stroke: 1.6px var(--ink);
  }

  .event-date {
    top: 722px; left: 174px;
    font-size: 72px;
    letter-spacing: 0.06em;
  }

  .event-time {
    top: 830px; left: 160px;
    display: flex; align-items: baseline;
  }
  .event-time .time-lead { font-size: 72px; letter-spacing: 0.06em; }
  .event-time .time-hour {
    font-family: "Arimo", sans-serif;
    font-weight: 700;
    font-size: 112px;
    color: var(--ink);
    -webkit-text-stroke: 0;
    margin-left: 26px;
    letter-spacing: 0.04em;
  }

  .access {
    top: 990px; left: 0; width: 1090px;
    text-align: center;
    font-weight: 700; font-size: 100px;
    letter-spacing: 0.04em;
    word-spacing: 0.3em;
  }

  .location-note {
    top: 1146px; left: 342px;
    font-size: 22px;
    letter-spacing: 0.1em;
    -webkit-text-stroke: 0.9px var(--muted);
  }

  .host-badge {
    top: 1130px; left: 848px;
    width: 268px; height: 70px;
    background: var(--badge);
    display: flex; align-items: center; justify-content: center;
    font-weight: 700; font-size: 17px;
    letter-spacing: 0.12em;
    color: var(--ink);
    text-transform: uppercase;
  }
</style>
</head>
<body>
  <main class="flyer">
    <p class="presenter">velvetroom atlanta presents</p>

    <svg class="club-mark" viewBox="0 0 190 190" aria-hidden="true">
      <circle cx="95" cy="95" r="88" fill="none" stroke="var(--mark)" stroke-width="10"/>
    </svg>

    <h1 class="club-name">
      <span class="name-main">Lanternfall</span>
      <span class="name-sub">Nightclub</span>
    </h1>

    <p class="tagline">a popup nightclub experience for one night only</p>

    <p class="event-date deco">Friday, October 18,2013</p>

    <p class="event-time">
      <span class="time-lead deco">Party begins at</span>
      <span class="time-hour">9PM</span>
    </p>

    <p class="access">invite only</p>

    <p class="location-note deco">See invitation for location details</p>

    <div class="host-badge">Velvetroom Atlanta</div>
  </main>
</body>
</html>
```